Business Card for a Wellness and Aesthetic Center

I'd like to have a business card design for a Wellness and Aesthetic Center based in the Philippines called "Silvermoss Wellness and Aesthetic Inc." They provide services such as medical and aesthetic dermatology. Specializing on cosmetic and anti-aging procedures.

The target market of the business is mostly women from the upper class from 30 to 60 years old.

The feel and look of the card should be feminine, modern, minimalist and classy.

The colors to play with are gold and black.

The front part should contain:
- Name (example: Marisol Teravid Pangilan, MD)
- Designation (example: Medical Director)
- Company Logo

The back part should contain:
- Company Logo
- Address
- Contact Details
- Website

For more details and inspiration you may visit their website at http://silvermossph.com/

Thank you very much!

Target Market(s)

Women from the upper class from 30 to 60 years old.

Industry/Entity Type

Business

Contact Information for Business Card

- Company Logo

- Company Logo
- Address
- Contact Details
- Website

Font styles to use
Serif
Script

Colors
ffc214
fece3e
faa54b
f78f20
000000

Requirements
Must have
• Design should be feminine, modern, minimalist/simple and classy.
Nice to have
• You can play with lines, curves, gardient and be creative on the placement of texts and logo.
Should not have
• Pictures like body, face or nature scene.

```html
<!DOCTYPE html>
<html lang="en">
<head>
<meta charset="utf-8">
<title>Silvermoss Wellness and Aesthetic Inc. — Business Card</title>
<link href="https://fonts.googleapis.com/css2?family=Lora:wght@400;500&display=swap" rel="stylesheet">
<style>
  :root {
    --page-bg: #ecebe7;
    --card-black: #222222;
    --card-charcoal: #464646;
    --gold: #e6d88c;
    --gold-light: #f7f1bd;
    --gold-deep: #d8c77a;
    --ink-white: #f4f4f2;
    --ink-grey: #e2e2e2;
    --ink-dark: #2a2a2a;
  }
  * { margin: 0; padding: 0; box-sizing: border-box; }
  html, body { width: 1200px; height: 1000px; overflow: hidden; }
  body {
    background: var(--page-bg);
    font-family: "Lora", Georgia, serif;
    position: relative;
  }
  .card {
    position: absolute;
    top: 150px;
    width: 400px;
    height: 700px;
    overflow: hidden;
    box-shadow: 0 6px 18px rgba(0,0,0,0.18);
  }
  /* Back side */
  .card-back {
    left: 160px;
    background: var(--card-black);
    color: var(--ink-white);
    text-align: center;
  }
  .brand-mark {
    position: absolute;
    left: 0; right: 0;
    top: 230px;
    font-size: 44px;
    font-weight: 400;
    color: var(--gold);
    letter-spacing: 1px;
  }
  .contact-list {
    position: absolute;
    left: 0; right: 0;
    top: 440px;
    font-size: 17px;
    line-height: 1.35;
  }
  .contact-item { margin-bottom: 18px; }
  .contact-icon {
    display: block;
    margin: 0 auto 8px;
    width: 18px; height: 18px;
  }
  /* Front side */
  .card-front {
    left: 640px;
    background: var(--card-charcoal);
  }
  .person {
    position: absolute;
    left: 0; right: 0;
    top: 260px;
    text-align: center;
  }
  .person-name {
    font-size: 19px;
    color: var(--gold);
    letter-spacing: 0.5px;
    text-transform: uppercase;
  }
  .person-title {
    font-size: 19px;
    color: var(--ink-grey);
    margin-top: 2px;
  }
  .gold-wave {
    position: absolute;
    left: 0; top: 0;
    width: 400px; height: 700px;
  }
  .brand-mark-front {
    position: absolute;
    right: 30px;
    top: 545px;
    font-size: 30px;
    color: var(--ink-dark);
  }
</style>
</head>
<body>

  <section class="card card-back" aria-label="Card back">
    <div class="brand-mark">Silvermoss</div>

    <div class="contact-list">
      <div class="contact-item address">
        <svg class="contact-icon" viewBox="0 0 24 24" aria-hidden="true">
          <path d="M12 2a7 7 0 0 0-7 7c0 5 7 13 7 13s7-8 7-13a7 7 0 0 0-7-7zm0 9.5A2.5 2.5 0 1 1 12 6.5a2.5 2.5 0 0 1 0 5z" fill="var(--gold)"/>
        </svg>
        Ground Floor, Lumen Crest Tower<br>
        Orchard Bay Business Park<br>
        Molave, Laguna Heights, PH
      </div>
      <div class="contact-item phone">
        <svg class="contact-icon" viewBox="0 0 24 24" aria-hidden="true">
          <path d="M6.6 10.8a15 15 0 0 0 6.6 6.6l2.2-2.2a1 1 0 0 1 1-.25 11.4 11.4 0 0 0 3.6.57 1 1 0 0 1 1 1V20a1 1 0 0 1-1 1A17 17 0 0 1 3 4a1 1 0 0 1 1-1h3.5a1 1 0 0 1 1 1c0 1.25.2 2.45.57 3.6a1 1 0 0 1-.25 1z" fill="var(--gold)"/>
        </svg>
        (632) 418-0936
      </div>
      <div class="contact-item web">
        <svg class="contact-icon" viewBox="0 0 24 24" aria-hidden="true">
          <g fill="none" stroke="var(--gold)" stroke-width="1.6">
            <circle cx="12" cy="12" r="9"/>
            <ellipse cx="12" cy="12" rx="4" ry="9"/>
            <path d="M3 12h18M4.5 7.5h15M4.5 16.5h15"/>
          </g>
        </svg>
        www.silvermossph.com
      </div>
    </div>
  </section>

  <section class="card card-front" aria-label="Card front">
    <div class="person">
      <p class="person-name">Marisol Teravid Pangilan, MD</p>
      <p class="person-title">Medical Director</p>
    </div>

    <svg class="gold-wave" viewBox="0 0 400 700" aria-hidden="true">
      <defs>
        <linearGradient id="goldSweep" x1="0" y1="0" x2="1" y2="0">
          <stop offset="0" stop-color="var(--gold-deep)"/>
          <stop offset="0.45" stop-color="var(--gold-light)"/>
          <stop offset="1" stop-color="var(--gold-deep)"/>
        </linearGradient>
      </defs>
      <path d="M0 440 C40 540 110 560 175 540 C265 508 320 405 400 385 L400 700 L0 700 Z" fill="url(#goldSweep)"/>
    </svg>

    <div class="brand-mark-front">Silvermoss</div>
  </section>

</body>
</html>
```